Wattle Groundworks Flyer

I would like to purchase a customized version of a design you have previously submitted - https://www.artpitchhub.net/design/8843290
Hello,
I like this design a lot. I would change the bullet points to;
- Landscape Design & Construction
- Paver Patio/path installations
- Retaining wall installations
- Pergola Installations
- Grading
- All Hardscape construction
- Drainage specialist
- Yard Maintenance plans
- Mulch & Pine needles
- Rooted Fine Service!
In the yellow star part - "Mention this flyer for a 10% discount!"
Phone number - 7045182409
email - wattlegroundworks@mailzen.net
website - www.wattlegroundworks.net
Target Market(s)
Residential homes in Charlotte, North Carolina
Industry/Entity Type
Landscaping
Look and feel
Each slider illustrates characteristics of the customer's brand and the style your logo design should communicate.

```html
<!DOCTYPE html>
<html lang="en">
<head>
<meta charset="utf-8">
<title>Wattle Groundworks Flyer</title>
<link rel="stylesheet" href="https://fonts.googleapis.com/css2?family=Alfa+Slab+One&family=Source+Sans+3:wght@600;700;800&family=Merriweather:wght@700&display=swap">
<style>
  :root {
    --canvas: #e8e8e4;
    --paper-top: #e6f0d8;
    --paper-bottom: #d3e6bd;
    --leaf: #3f9a2a;
    --leaf-dark: #2a7a1e;
    --forest: #1d5a16;
    --ink: #1f2419;
    --bark: #4a2f18;
    --rust: #a5561b;
    --copper: #b06a2a;
    --white: #ffffff;
  }
  * { margin: 0; padding: 0; box-sizing: border-box; }
  html, body { width: 1200px; height: 800px; overflow: hidden; background: var(--canvas); }
  .flyer {
    position: absolute; left: 294px; top: 4px;
    width: 612px; height: 792px; overflow: hidden;
    font-family: "Source Sans 3", sans-serif;
    box-shadow: 0 2px 10px rgba(0,0,0,.18);
  }
  .flyer-art { position: absolute; inset: 0; }
  .brand {
    position: absolute; left: 30px; top: 52px;
    display: flex; align-items: center; gap: 10px;
  }
  .brand-dot { width: 34px; height: 34px; border-radius: 50%; background: var(--bark); }
  .brand-name {
    font-weight: 800; font-size: 21px; line-height: 23px; letter-spacing: 2px;
    color: var(--bark); text-transform: uppercase;
  }
  .headline {
    position: absolute; left: 240px; width: 370px; top: 40px;
    font-family: "Alfa Slab One", serif; font-weight: 400; font-size: 36px; line-height: 42px;
    color: var(--leaf); text-align: center; white-space: nowrap;
    text-shadow: 0 1px 0 #1f6a14, 0 2px 3px rgba(0,0,0,.25);
  }
  .tagline {
    position: absolute; left: 245px; width: 350px; top: 137px;
    font-weight: 700; font-size: 13px; line-height: 17px;
    color: var(--rust); text-align: center; text-transform: uppercase;
  }
  .services-title {
    position: absolute; left: 22px; top: 480px;
    font-family: "Alfa Slab One", serif; font-weight: 400; font-size: 28px;
    color: var(--leaf); text-shadow: 0 1px 0 #1f6a14;
  }
  .service {
    position: absolute; width: 150px;
    display: flex; align-items: center; gap: 8px;
    font-weight: 700; font-size: 12px; line-height: 14px;
    color: var(--ink); text-transform: uppercase;
  }
  .service-icon { flex: none; width: 30px; height: 30px; }
  .discount-text {
    position: absolute; left: 477px; top: 669px; width: 110px;
    font-family: "Merriweather", serif; font-weight: 700; font-size: 11.5px; line-height: 19px;
    color: var(--white); text-align: center; white-space: nowrap;
  }
  .phone {
    position: absolute; left: 175px; top: 718px; width: 250px; height: 42px;
    display: flex; align-items: center; justify-content: center; gap: 6px;
    font-weight: 800; font-size: 25px; color: var(--white); letter-spacing: .5px;
  }
  .contact-row {
    position: absolute; left: 0; right: 0; top: 765px;
    display: flex; justify-content: center; gap: 20px;
    font-weight: 700; font-size: 15px; color: var(--white);
  }
  .contact-item { display: flex; align-items: center; gap: 8px; }
</style>
</head>
<body>
<div class="flyer">
  <svg class="flyer-art" width="612" height="792" viewBox="0 0 612 792">
    <defs>
      <linearGradient id="paper" x1="0" y1="0" x2="0" y2="1">
        <stop offset="0" stop-color="#e6f0d8"/><stop offset="1" stop-color="#d3e6bd"/>
      </linearGradient>
      <linearGradient id="garden" x1="0" y1="0" x2="1" y2="1">
        <stop offset="0" stop-color="#8a8e6c"/><stop offset=".45" stop-color="#5f8a3c"/><stop offset="1" stop-color="#3f6b28"/>
      </linearGradient>
      <linearGradient id="footer" x1="0" y1="0" x2="0" y2="1">
        <stop offset="0" stop-color="#5cb844"/><stop offset="1" stop-color="#2f8a24"/>
      </linearGradient>
      <radialGradient id="seal" cx=".45" cy=".4" r=".7">
        <stop offset="0" stop-color="#c98440"/><stop offset="1" stop-color="#9a5a22"/>
      </radialGradient>
    </defs>
    <rect width="612" height="792" fill="url(#paper)"/>

    <path role="img" aria-label="Photo of a landscaped front garden with stone steps, shrubs and flower beds"
      d="M0,180 C150,198 300,238 410,232 C480,228 560,206 612,182 L612,640 C560,600 520,500 420,445 C330,410 150,420 0,478 Z" fill="url(#garden)"/>
    <path d="M0,160 C150,182 300,228 410,218 C490,211 565,185 612,160 L612,182 C560,206 480,228 410,232 C300,238 150,198 0,180 Z" fill="var(--leaf-dark)"/>
    <path d="M0,180 C150,198 300,238 410,232 C480,228 560,206 612,182" fill="none" stroke="#6cc24a" stroke-width="3"/>
    <path d="M0,478 C150,420 330,410 420,445 C520,500 560,600 612,640 L612,650 C555,610 515,512 418,458 C330,422 150,432 0,492 Z" fill="var(--leaf-dark)"/>
    <path d="M0,492 C150,432 330,422 418,458" fill="none" stroke="#6cc24a" stroke-width="3"/>

    <circle role="img" aria-label="Photo of a timber pergola beside a swimming pool" cx="405" cy="463" r="105" fill="#8d7d5c" stroke="#e8f3dc" stroke-width="4"/>
    <circle role="img" aria-label="Photo of a stepping-stone path across a lawn" cx="492" cy="570" r="85" fill="#6f8a4c" stroke="#e8f3dc" stroke-width="4"/>
    <circle role="img" aria-label="Photo of a stone retaining wall and garden bed" cx="385" cy="624" r="65" fill="#6b5a45" stroke="#e8f3dc" stroke-width="4"/>

    <polygon fill="url(#seal)" points="
      532,640 540,652 553,645 556,659 571,658 568,672 582,676 574,688 587,698 574,708 582,720 568,724 571,738 556,737 553,751 540,744 532,756 524,744 511,751 508,737 493,738 496,724 482,720 490,708 477,698 490,688 482,676 496,672 493,658 508,659 511,645 524,652"/>

    <path d="M0,752 C150,742 450,742 612,750 L612,792 L0,792 Z" fill="url(#footer)"/>
    <path d="M185,718 L415,718 Q425,718 425,728 L425,760 L175,760 L175,728 Q175,718 185,718 Z" fill="var(--forest)"/>
  </svg>

  <div class="brand">
    <span class="brand-dot"></span>
    <span class="brand-name">Wattle<br>Groundworks</span>
  </div>

  <h1 class="headline">Rooted Fine<br>Service!</h1>
  <p class="tagline">Dipendable professionals dedicated<br>to the quality of your property.</p>

  <h2 class="services-title">Our services</h2>

  <div class="service" style="left:14px;top:520px"><svg class="service-icon" viewBox="0 0 30 30"><circle cx="15" cy="15" r="14" fill="#7ccf5a"/><circle cx="15" cy="15" r="11" fill="#2a7a1e"/><path d="M9,15 l4,4 l8,-8" fill="none" stroke="#fff" stroke-width="2.4"/></svg>Landscape design &amp; construction</div>
  <div class="service" style="left:14px;top:557px"><svg class="service-icon" viewBox="0 0 30 30"><circle cx="15" cy="15" r="14" fill="#7ccf5a"/><circle cx="15" cy="15" r="11" fill="#2a7a1e"/><path d="M9,15 l4,4 l8,-8" fill="none" stroke="#fff" stroke-width="2.4"/></svg>Paver patio/path installations</div>
  <div class="service" style="left:14px;top:594px"><svg class="service-icon" viewBox="0 0 30 30"><circle cx="15" cy="15" r="14" fill="#7ccf5a"/><circle cx="15" cy="15" r="11" fill="#2a7a1e"/><path d="M9,15 l4,4 l8,-8" fill="none" stroke="#fff" stroke-width="2.4"/></svg>Retaining wall installations</div>
  <div class="service" style="left:14px;top:628px"><svg class="service-icon" viewBox="0 0 30 30"><circle cx="15" cy="15" r="14" fill="#7ccf5a"/><circle cx="15" cy="15" r="11" fill="#2a7a1e"/><path d="M9,15 l4,4 l8,-8" fill="none" stroke="#fff" stroke-width="2.4"/></svg>Pergola installations</div>
  <div class="service" style="left:14px;top:663px"><svg class="service-icon" viewBox="0 0 30 30"><circle cx="15" cy="15" r="14" fill="#7ccf5a"/><circle cx="15" cy="15" r="11" fill="#2a7a1e"/><path d="M9,15 l4,4 l8,-8" fill="none" stroke="#fff" stroke-width="2.4"/></svg>Grading</div>

  <div class="service" style="left:165px;top:520px"><svg class="service-icon" viewBox="0 0 30 30"><circle cx="15" cy="15" r="14" fill="#7ccf5a"/><circle cx="15" cy="15" r="11" fill="#2a7a1e"/><path d="M9,15 l4,4 l8,-8" fill="none" stroke="#fff" stroke-width="2.4"/></svg>All hardscape construction</div>
  <div class="service" style="left:165px;top:557px"><svg class="service-icon" viewBox="0 0 30 30"><circle cx="15" cy="15" r="14" fill="#7ccf5a"/><circle cx="15" cy="15" r="11" fill="#2a7a1e"/><path d="M9,15 l4,4 l8,-8" fill="none" stroke="#fff" stroke-width="2.4"/></svg>Drainage specialist</div>
  <div class="service" style="left:165px;top:594px"><svg class="service-icon" viewBox="0 0 30 30"><circle cx="15" cy="15" r="14" fill="#7ccf5a"/><circle cx="15" cy="15" r="11" fill="#2a7a1e"/><path d="M9,15 l4,4 l8,-8" fill="none" stroke="#fff" stroke-width="2.4"/></svg>Yard maintenance plans</div>
  <div class="service" style="left:165px;top:628px"><svg class="service-icon" viewBox="0 0 30 30"><circle cx="15" cy="15" r="14" fill="#7ccf5a"/><circle cx="15" cy="15" r="11" fill="#2a7a1e"/><path d="M9,15 l4,4 l8,-8" fill="none" stroke="#fff" stroke-width="2.4"/></svg>Mulch &amp; pine needles</div>
  <div class="service" style="left:165px;top:663px"><svg class="service-icon" viewBox="0 0 30 30"><circle cx="15" cy="15" r="14" fill="#7ccf5a"/><circle cx="15" cy="15" r="11" fill="#2a7a1e"/><path d="M9,15 l4,4 l8,-8" fill="none" stroke="#fff" stroke-width="2.4"/></svg>Rooted Fine Service!</div>

  <p class="discount-text">Mention this<br>flyer for a<br>10% discount!</p>

  <div class="phone">
    <svg width="20" height="24" viewBox="0 0 20 24"><rect x="3" y="1" width="14" height="22" rx="3" fill="none" stroke="#fff" stroke-width="2.2"/><line x1="8" y1="19" x2="12" y2="19" stroke="#fff" stroke-width="2"/></svg>
    704 518 2409
  </div>

  <div class="contact-row">
    <span class="contact-item"><svg width="14" height="14" viewBox="0 0 14 14"><circle cx="7" cy="7" r="7" fill="#fff"/><rect x="3.5" y="4.5" width="7" height="5" fill="none" stroke="#2f8a24" stroke-width="1"/><path d="M3.5,4.5 L7,7.5 L10.5,4.5" fill="none" stroke="#2f8a24" stroke-width="1"/></svg>wattlegroundworks@mailzen.net</span>
    <span class="contact-item"><svg width="14" height="14" viewBox="0 0 14 14"><circle cx="7" cy="7" r="7" fill="#fff"/><circle cx="7" cy="7" r="4" fill="none" stroke="#2f8a24" stroke-width="1"/><line x1="3" y1="7" x2="11" y2="7" stroke="#2f8a24" stroke-width="1"/><ellipse cx="7" cy="7" rx="1.8" ry="4" fill="none" stroke="#2f8a24" stroke-width="1"/></svg>www.wattlegroundworks.net</span>
  </div>
</div>
</body>
</html>
```